Bref créative
Harbor Floors & More --- Business card
Harbor Floors & More - thousands of types of tiles
Simple
Mei Dalton
4150 Marwood Ave,
Unit 3B, Concord, ON
L4K 5R8
mei.dalton@harborfloorsmore.example
www.harborfloorsmore.example
Introduction : Harbor Floors & More imports and distributes thousands of types of tiles in limestone, marble, slate, granite, porcelan, ceramic, glass and aluminum for homeowners, builders and contractors. Also providing custom-made solid wood kitchen cabinet and vanities.
the logo of Harbor Floors & More
Logo on Black
Logo on White

```html
<!DOCTYPE html>
<html lang="en">
<head>
<meta charset="utf-8">
<title>Harbor Floors &amp; More — Stationery</title>
<link rel="stylesheet" href="https://fonts.googleapis.com/css2?family=Open+Sans:wght@400;600&display=swap">
<style>
:root{
  --bg:#eceeef;
  --paper:#ffffff;
  --ink:#111214;
  --blue:#1fa3e0;
  --blue-dark:#0a6fb8;
  --green:#b9d433;
  --grey:#6b6f73;
  --shadow:0 4px 12px rgba(0,0,0,.18);
}
*{margin:0;padding:0;box-sizing:border-box}
html,body{width:1200px;height:936px;overflow:hidden;background:var(--bg);font-family:"Open Sans",Arial,sans-serif}
.canvas{position:relative;width:1200px;height:936px}
.item{position:absolute;box-shadow:var(--shadow);overflow:hidden}
.item svg.wave{position:absolute;left:0;width:100%}
.brand{display:flex;align-items:center;gap:8px;font-weight:600;text-transform:uppercase;letter-spacing:.02em;line-height:1.05;white-space:nowrap}
.brand .mark{width:12px;height:12px;background:var(--blue);flex:none}
.brand--light{color:#fff}

/* Letterhead */
.letterhead{left:183px;top:56px;width:388px;height:553px;background:var(--paper)}
.letterhead .head-wave{top:0;height:70px}
.letterhead .brand{position:absolute;left:18px;top:14px;font-size:13px}
.letterhead .watermark{position:absolute;left:0;right:0;top:240px;text-align:center;font-size:22px;font-weight:600;color:#dfeef6;text-transform:uppercase}
.letterhead .contact{position:absolute;left:22px;bottom:24px;font-size:6px;line-height:1.6;color:var(--grey)}
.contact .dot{display:inline-block;width:4px;height:4px;background:var(--green);margin-right:4px;vertical-align:middle}

/* Folder */
.folder{left:634px;top:38px;width:394px;height:576px;background:var(--ink)}
.folder .brand{position:absolute;left:0;right:0;top:255px;justify-content:center;font-size:30px;font-weight:400}
.folder .brand .mark{width:22px;height:22px}
.folder .foot-wave{bottom:0;height:100px}

/* Business cards */
.card{left:33px;width:208px;height:110px;background:var(--ink)}
.card--front{top:642px}
.card--back{top:790px}
.card--front .brand{position:absolute;left:12px;top:18px;font-size:9px}
.card--front .brand .mark{width:8px;height:8px}
.card--front .details{position:absolute;left:12px;top:46px;font-size:5px;line-height:1.55;color:#cfd3d6}
.card--front .details strong{color:#fff;font-weight:600}
.card--back .brand{position:absolute;left:0;right:0;top:36px;justify-content:center;font-size:9px}
.card--back .brand .mark{width:8px;height:8px}
.card--back .web{position:absolute;left:0;right:0;top:66px;text-align:center;font-size:5px;color:#cfd3d6}
.card .foot-wave{bottom:0;height:26px}

/* Envelope front */
.envelope{left:271px;top:660px;width:427px;height:241px;background:var(--paper)}
.envelope .head-wave{top:0;height:62px}
.envelope .brand{position:absolute;left:18px;top:14px;font-size:12px}

/* Envelope back */
.envelope-back{left:736px;top:675px;width:436px;height:226px;background:var(--paper)}
.envelope-back .flap{position:absolute;left:0;top:0;width:100%;height:60px;background:linear-gradient(180deg,var(--blue),var(--blue-dark))}
.envelope-back .web{position:absolute;left:0;right:0;top:22px;text-align:center;font-size:9px;letter-spacing:.25em;color:#fff}
</style>
</head>
<body>
<main class="canvas">

  <section class="item letterhead">
    <svg class="wave head-wave" viewBox="0 0 388 70" preserveAspectRatio="none" aria-hidden="true">
      <path d="M0 0H388V20C300 48 170 30 0 48Z" fill="#111214"/>
      <path d="M0 48C170 30 300 48 388 20V30C300 58 170 42 0 56Z" fill="#1fa3e0"/>
      <path d="M0 56C170 42 300 58 388 30V34C300 62 170 48 0 60Z" fill="#b9d433"/>
    </svg>
    <div class="brand brand--light"><span class="mark"></span><span>Harbor Floors<br>&amp; More</span></div>
    <div class="watermark">Harbor Floors &amp; More</div>
    <div class="contact">
      <div><span class="dot"></span>4150 Marwood Ave, Unit 3B, Concord, ON L4K 5R8</div>
      <div><span class="dot"></span>T 905 555 0142</div>
      <div><span class="dot"></span>mei.dalton@harborfloorsmore.example</div>
      <div><span class="dot"></span>www.harborfloorsmore.example</div>
    </div>
  </section>

  <section class="item folder">
    <div class="brand brand--light"><span class="mark"></span><span>Harbor Floors<br>&amp; More</span></div>
    <svg class="wave foot-wave" viewBox="0 0 394 100" preserveAspectRatio="none" aria-hidden="true">
      <path d="M0 40C120 10 260 70 394 30V100H0Z" fill="#b9d433"/>
      <path d="M0 55C140 25 260 85 394 45V100H0Z" fill="#1fa3e0"/>
      <path d="M0 68C140 40 260 95 394 62V100H0Z" fill="#0a6fb8"/>
    </svg>
  </section>

  <section class="item card card--front">
    <div class="brand brand--light"><span class="mark"></span><span>Harbor Floors<br>&amp; More</span></div>
    <div class="details">
      <div><strong>Mei Dalton</strong> · Sales Manager</div>
      <div>4150 Marwood Ave, Unit 3B, Concord, ON L4K 5R8</div>
      <div>T 905 555 0142</div>
      <div>mei.dalton@harborfloorsmore.example</div>
    </div>
  </section>

  <section class="item card card--back">
    <div class="brand brand--light"><span class="mark"></span><span>Harbor Floors<br>&amp; More</span></div>
    <div class="web">www.harborfloorsmore.example</div>
    <svg class="wave foot-wave" viewBox="0 0 208 26" preserveAspectRatio="none" aria-hidden="true">
      <path d="M0 12C70 0 140 24 208 8V26H0Z" fill="#1fa3e0"/>
      <path d="M0 18C70 8 140 28 208 16V26H0Z" fill="#0a6fb8"/>
    </svg>
  </section>

  <section class="item envelope">
    <svg class="wave head-wave" viewBox="0 0 427 62" preserveAspectRatio="none" aria-hidden="true">
      <path d="M0 0H427V22C320 50 180 28 0 44Z" fill="#111214"/>
      <path d="M0 44C180 28 320 50 427 22V32C320 58 180 40 0 52Z" fill="#1fa3e0"/>
      <path d="M0 52C180 40 320 58 427 32V36C320 62 180 46 0 56Z" fill="#b9d433"/>
    </svg>
    <div class="brand brand--light"><span class="mark"></span><span>Harbor Floors<br>&amp; More</span></div>
  </section>

  <section class="item envelope-back">
    <div class="flap"></div>
    <div class="web">www.harborfloorsmore.example</div>
  </section>

</main>
</body>
</html>
```